TAVRO Capital Group LLC a High Risk Big Rewards company for Rich Young Entrepreneurs

We would like a very modern, powerful in the eyes of our customers, modern, minimalist feel, financial gain. this business card is for young Rich entrepreneurs who want to invest money into High Risk, Big Rewards Businesses. The card Should sell the business!! let your creativity go Wild! I pick most of the designers for this project because of your BOLD Designs, I would like this card to be Bold, Modern, Minimalist, use as many effects in your graphic Artist Mind, Do not let the Financial sound of this business to make you think Conservative that's the last thing we are! if you have a lot of money and you want to play a risky market call US
Updates

Project Deadline Extended
Reason: have not received, enough designs to choose 1st and second place, sure I have received over 100 designs but it seems most designers are submitting every card they have ever made before and calling it mine, please we are looking for fresh ideas please!

Target Market(s)

Private Risky Investors

Industry/Entity Type

Financial

Contact Information for Business Card

powerful in the eyes of our customers,modern, minimalist feel

Font styles to use
Other font styles liked:
• Modern feeling fonts

Requirements
Must have
• The Company Name is TAVRO Capital Group LLC and it must be on the CARD
• My Name, title, Cell , email
• Delvin Ashcroft G.E.D.
• Managing Member
• 555.038.6195
• delvin@tavrocapitalgroup.example
Nice to have
• try a black thick plastic card with round corners with Delvin Ashcroft GED (make sure GED is smaller than name) just on one side of the card, and my phone number with out the icons and email on the other side, this card should look like a exclusive credit card or exclusive VIP card, something you would never loose

```html
<!DOCTYPE html>
<html lang="en">
<head>
<meta charset="utf-8">
<title>TAVRO Capital Group LLC — Business Card</title>
<link rel="stylesheet" href="https://fonts.googleapis.com/css2?family=Bebas+Neue&family=Pathway+Gothic+One&display=swap">
<style>
  :root {
    --page-bg: #e7e5e2;
    --orange: #ec8148;
    --red: #c7373a;
    --band-white: #f1f0ec;
    --ink-grey: #4a4a4a;
    --charcoal-top: #3c3c3c;
    --charcoal-bottom: #262626;
    --white: #ffffff;
  }
  * { margin: 0; padding: 0; box-sizing: border-box; }
  html, body {
    width: 1200px;
    height: 1000px;
    overflow: hidden;
    background: var(--page-bg);
  }
  .canvas {
    position: relative;
    width: 1200px;
    height: 1000px;
  }
  .card {
    position: absolute;
    left: 250px;
    width: 700px;
    height: 400px;
    border-radius: 6px;
    overflow: hidden;
    box-shadow: 0 10px 26px rgba(0,0,0,0.18);
  }

  /* Front */
  .card--front {
    top: 70px;
    background: linear-gradient(100deg, var(--orange) 0%, #de6a48 45%, var(--red) 100%);
  }
  .contact-rows {
    position: absolute;
    right: 36px;
    top: 176px;
    display: grid;
    grid-template-columns: auto auto;
    column-gap: 0;
    font-family: "Pathway Gothic One", "Arial Narrow", sans-serif;
    color: var(--white);
    font-size: 22px;
    line-height: 26px;
    letter-spacing: 0.5px;
    text-transform: uppercase;
  }
  .contact-rows .contact-left {
    text-align: right;
    padding-right: 10px;
    border-right: 1.5px solid var(--white);
  }
  .contact-rows .contact-right {
    text-align: left;
    padding-left: 10px;
  }
  .holder-name {
    font-family: "Bebas Neue", "Arial Narrow", sans-serif;
    font-size: 26px;
    letter-spacing: 1px;
  }
  .holder-name .credential { font-size: 20px; }
  .white-band {
    position: absolute;
    left: 0;
    right: 0;
    top: 238px;
    height: 112px;
    background: var(--band-white);
    text-align: right;
    padding: 10px 36px 0 0;
  }
  .company-name {
    font-family: "Bebas Neue", "Arial Narrow", sans-serif;
    font-size: 52px;
    line-height: 50px;
    letter-spacing: 1px;
  }
  .company-tagline {
    font-family: "Bebas Neue", "Arial Narrow", sans-serif;
    font-size: 27px;
    line-height: 28px;
    letter-spacing: 0.5px;
  }
  .white-band .company-name,
  .white-band .company-tagline { color: var(--ink-grey); }

  /* Back */
  .card--back {
    top: 530px;
    background: linear-gradient(180deg, var(--charcoal-top) 0%, var(--charcoal-bottom) 100%);
  }
  .orange-band {
    position: absolute;
    left: 0;
    right: 0;
    top: 222px;
    height: 100px;
    background: linear-gradient(100deg, var(--orange) 0%, var(--red) 100%);
    text-align: right;
    padding: 10px 36px 0 0;
  }
  .orange-band .company-name,
  .orange-band .company-tagline { color: var(--white); }
  .orange-band .company-name { font-size: 48px; line-height: 46px; }
  .orange-band .company-tagline { font-size: 25px; line-height: 26px; }
</style>
</head>
<body>
<main class="canvas">

  <section class="card card--front" aria-label="Business card front">
    <div class="contact-rows">
      <span class="contact-left">555.038.6195</span>
      <span class="contact-right">Managing Member</span>
      <span class="contact-left">delvin@tavrocapitalgroup.example</span>
      <span class="contact-right holder-name">Delvin Ashcroft <span class="credential">G.E.D</span></span>
    </div>
    <div class="white-band">
      <p class="company-name">TAVRO CAPITAL GROUP LLC</p>
      <p class="company-tagline">A DOMESTIC LIMITED LIABILITY COMPANY</p>
    </div>
  </section>

  <section class="card card--back" aria-label="Business card back">
    <div class="orange-band">
      <p class="company-name">TAVRO CAPITAL GROUP LLC</p>
      <p class="company-tagline">A DOMESTIC LIMITED LIABILITY COMPANY</p>
    </div>
  </section>

</main>
</body>
</html>
```